Business Card Design Project

I would like to have a project of business card with incorporated attachted logo elements in warm colors like: gold, yellow, brown.
We would like incorporate below information into the design
Name of the Company: Continental Hoop Invitational
Name: Dorian Pelkey
Position: Project Director
e-mail: dorian@hoopinvitational.net
mobile: +65 83147092
website: www.hoopinvitational.net
Address: 47 Marbury Lane, #06-11, Singapore 915274
There is a picture attachted which can be used as a back side of the buisness card - we would like to follow the colors theme on the front card ( with the person contact details) how ever the front card we will prefer with white background but with graphfic elements coming from logo.
Project Deadline Extended
Reason: the project has been launched on 24 of April with deadline by 24 of April by mistakes. Thats why I would like to extend the deadline.
Name: Dorian Pelkey
mobile: +65 83147092

```html
<!DOCTYPE html>
<html lang="en">
<head>
<meta charset="utf-8">
<title>Continental Hoop Invitational – Business Card</title>
<link href="https://fonts.googleapis.com/css2?family=Jost:wght@400&family=Courier+Prime:wght@700&display=swap" rel="stylesheet">
<style>
  :root {
    --brown: #9a3f00;
    --yellow: #ffff00;
    --yellow-text: #f2ee00;
    --ink: #141414;
    --paper: #ffffff;
  }
  html, body {
    margin: 0;
    padding: 0;
    overflow: hidden;
    background: var(--paper);
  }
  .card {
    position: relative;
    width: 1200px;
    height: 686px;
    background: var(--paper);
    overflow: hidden;
    font-family: "Jost", "Futura", sans-serif;
  }
  .contact-person {
    position: absolute;
    right: 57px;
    top: 44px;
    text-align: right;
    color: var(--ink);
  }
  .contact-person__name {
    margin: 0;
    font-size: 41px;
    font-weight: 400;
    line-height: 1;
    color: var(--brown);
  }
  .contact-person__role,
  .contact-person__mobile {
    margin: 0;
    font-size: 30px;
    line-height: 1.5;
  }
  .contact-person__role { margin-top: 6px; }
  .company-name {
    position: absolute;
    left: 42px;
    top: 268px;
    margin: 0;
    font-family: "Courier Prime", "Courier New", monospace;
    font-weight: 700;
    font-size: 56px;
    line-height: 1;
    color: var(--brown);
    white-space: nowrap;
  }
  .company-name__gap { display: inline-block; width: 126px; }
  .divider {
    position: absolute;
    left: 490px;
    top: 278px;
  }
  .band {
    position: absolute;
    top: 560px;
    height: 126px;
  }
  .band--address {
    left: 0;
    width: 499px;
    background: var(--brown);
  }
  .band--web {
    left: 501px;
    right: 0;
    background: var(--yellow);
  }
  .address-label {
    position: absolute;
    left: 42px;
    top: 518px;
    margin: 0;
    font-size: 27px;
    color: var(--brown);
  }
  .address {
    position: absolute;
    left: 42px;
    top: 567px;
    margin: 0;
    font-style: normal;
    font-size: 29px;
    line-height: 45px;
    color: var(--paper);
  }
  .online {
    position: absolute;
    right: 46px;
    top: 567px;
    margin: 0;
    text-align: right;
    font-size: 29px;
    line-height: 45px;
    color: var(--ink);
  }
</style>
</head>
<body>
<main class="card">
  <section class="contact-person">
    <h1 class="contact-person__name">Dorian Pelkey</h1>
    <p class="contact-person__role">Project Direction</p>
    <p class="contact-person__mobile">Mobile : +65 83147092</p>
  </section>

  <h2 class="company-name">Continental<span class="company-name__gap"></span>Hoop Invitational</h2>

  <svg class="divider" width="14" height="282" viewBox="0 0 14 282" aria-hidden="true">
    <line x1="7" y1="0" x2="7" y2="282" stroke="var(--yellow-text)" stroke-width="4" stroke-dasharray="16 32"/>
    <line x1="7" y1="24" x2="7" y2="282" stroke="var(--brown)" stroke-width="4" stroke-dasharray="16 32"/>
  </svg>

  <div class="band band--address"></div>
  <div class="band band--web"></div>

  <p class="address-label">Address:</p>
  <address class="address">47 Marbury Lane, #06-11,<br>Singapore 915274</address>

  <p class="online">E-mail : dorian@hoopinvitational.net<br>Website : www.hoopinvitational.net</p>
</main>
</body>
</html>
```